Visitenkarten-Design
Zielgruppe
Malerbetrieb
Zielgruppe: Private Haushalte, Hausverwaltungen
Aufgabenstellung
Logo ist vorhanden
Lorenz Saber
Malermeister

```html
<!DOCTYPE html>
<html lang="de">
<head>
<meta charset="utf-8">
<title>Malereibetrieb Saber – Visitenkarten</title>
<link rel="stylesheet" href="https://fonts.googleapis.com/css2?family=Open+Sans:wght@300;400;700&family=Oswald:wght@500;600&display=swap">
<style>
  :root {
    --page: #ffffff;
    --card-dark: #3a3a3c;
    --card-light: #f2f2f4;
    --ink-dark: #ffffff;
    --ink-light: #111111;
    --contact-light: #3a3a3c;
    --muted-light: #8a8a8c;
    --name-light: #5a5a5c;
    --cyan: #27a2dc;
    --yellow: #f4ec18;
    --magenta: #c5198c;
    --shadow: 8px 10px 14px rgba(0, 0, 0, 0.45);
  }
  * { margin: 0; padding: 0; box-sizing: border-box; }
  html, body { width: 1200px; height: 706px; overflow: hidden; background: var(--page); }
  .sheet { position: relative; width: 1200px; height: 706px; }

  .card {
    position: absolute; width: 368px; height: 206px; overflow: hidden;
    box-shadow: var(--shadow);
    font-family: "Open Sans", sans-serif;
  }
  .card.dark { background: var(--card-dark); color: var(--ink-dark); }
  .card.light { background: var(--card-light); color: var(--ink-light); }
  .card.front.dark { left: 164px; top: 79px; }
  .card.front.light { left: 584px; top: 79px; }
  .card.back.dark { left: 164px; top: 324px; }
  .card.back.light { left: 584px; top: 324px; }

  /* Brand lockup */
  .brand { position: absolute; left: 0; width: 100%; text-align: center; }
  .front .brand { top: 22px; }
  .brand-name { display: block; font-weight: 700; letter-spacing: 1px; line-height: 1; }
  .front .brand-name { font-size: 46px; }
  .brand-trade {
    display: block; font-weight: 300; font-size: 18.5px; line-height: 1;
    margin-top: 3px; letter-spacing: -0.2px;
  }
  .brand-claim {
    display: block; font-size: 8.4px; line-height: 1; margin-top: 3px;
    letter-spacing: 0.5px; white-space: nowrap;
  }
  .light .brand-claim { color: var(--muted-light); }

  /* Person */
  .person { position: absolute; left: 273px; top: 108px; font-family: "Oswald", sans-serif; line-height: 1; }
  .person-name { display: block; font-weight: 600; font-size: 15px; letter-spacing: 0.1px; white-space: nowrap; }
  .person-role { display: block; font-weight: 500; font-size: 9px; letter-spacing: 1px; margin-top: 3px; margin-left: 2px; }
  .light .person-name { color: var(--name-light); }
  .light .person-role { color: var(--muted-light); }

  /* Contact list */
  .contact { position: absolute; left: 19px; top: 130px; list-style: none; font-size: 8px; line-height: 10px; }
  .contact li { display: flex; align-items: flex-start; margin-bottom: 3.5px; }
  .contact li.address { margin-bottom: 5px; }
  .light .contact { color: var(--contact-light); }
  .icon { width: 9px; height: 9px; flex: none; margin-right: 11px; margin-top: 0.5px; }
  .dark .icon { color: var(--ink-dark); }
  .light .icon { color: var(--contact-light); }

  /* Colour strip along the bottom edge */
  .strip { position: absolute; left: 0; right: 0; bottom: 0; height: 6px; display: flex; }
  .strip span { flex: 1; }
  .strip .cyan { background: var(--cyan); }
  .strip .yellow { background: var(--yellow); }
  .strip .magenta { background: var(--magenta); }

  /* Back side */
  .back .brand { top: 50px; }
  .back .brand-name { font-size: 70px; letter-spacing: 2px; }
  .back .web {
    position: absolute; top: 131px; left: 0; width: 100%;
    display: flex; justify-content: center; align-items: center; font-size: 8px;
  }
  .back .web .icon { margin-top: 0; margin-right: 10px; }
  .light .web { color: var(--contact-light); }
</style>
</head>
<body>
<svg width="0" height="0" style="position:absolute" aria-hidden="true">
  <symbol id="i-home" viewBox="0 0 10 10"><circle cx="5" cy="5" r="5" fill="currentColor"/><path fill="#888" d="M3 7V4.6L5 3l2 1.6V7z"/></symbol>
  <symbol id="i-phone" viewBox="0 0 10 10"><circle cx="5" cy="5" r="5" fill="currentColor"/><path fill="none" stroke="#888" stroke-width="1.3" d="M3.3 3c0 2.2 1.5 3.7 3.7 3.9"/></symbol>
  <symbol id="i-mail" viewBox="0 0 10 10"><circle cx="5" cy="5" r="5" fill="currentColor"/><path fill="none" stroke="#888" stroke-width="0.9" d="M2.8 3.5h4.4v3H2.8zM2.8 3.5L5 5.3l2.2-1.8"/></symbol>
  <symbol id="i-web" viewBox="0 0 10 10"><circle cx="5" cy="5" r="5" fill="currentColor"/><g fill="none" stroke="#888" stroke-width="0.7"><circle cx="5" cy="5" r="2.6"/><path d="M2.4 5h5.2M5 2.4v5.2"/></g></symbol>
</svg>

<main class="sheet">
  <section class="card front dark">
    <div class="brand">
      <span class="brand-name">SABER</span>
      <span class="brand-trade">MALEREIBETRIEB</span>
      <span class="brand-claim">Sorgfalt ist unser schönster Farbton</span>
    </div>
    <div class="person">
      <span class="person-name">LORENZ SABER</span>
      <span class="person-role">MALERMEISTER</span>
    </div>
    <ul class="contact">
      <li class="address"><svg class="icon"><use href="#i-home"/></svg><span>Birkenweg 118 c,<br>48231 Lindmoor</span></li>
      <li><svg class="icon"><use href="#i-phone"/></svg><span>0172-5 318 204</span></li>
      <li><svg class="icon"><use href="#i-mail"/></svg><span>info@malereibetrieb-saber.de</span></li>
      <li><svg class="icon"><use href="#i-web"/></svg><span>www.malereibetrieb-saber.de</span></li>
    </ul>
    <div class="strip"><span class="cyan"></span><span class="yellow"></span><span class="magenta"></span></div>
  </section>

  <section class="card front light">
    <div class="brand">
      <span class="brand-name">SABER</span>
      <span class="brand-trade">MALEREIBETRIEB</span>
      <span class="brand-claim">Sorgfalt ist unser schönster Farbton</span>
    </div>
    <div class="person">
      <span class="person-name">LORENZ SABER</span>
      <span class="person-role">MALERMEISTER</span>
    </div>
    <ul class="contact">
      <li class="address"><svg class="icon"><use href="#i-home"/></svg><span>Birkenweg 118 c,<br>48231 Lindmoor</span></li>
      <li><svg class="icon"><use href="#i-phone"/></svg><span>0172-5 318 204</span></li>
      <li><svg class="icon"><use href="#i-mail"/></svg><span>info@malereibetrieb-saber.de</span></li>
      <li><svg class="icon"><use href="#i-web"/></svg><span>www.malereibetrieb-saber.de</span></li>
    </ul>
    <div class="strip"><span class="cyan"></span><span class="yellow"></span><span class="magenta"></span></div>
  </section>

  <section class="card back dark">
    <div class="brand"><span class="brand-name">SABER</span></div>
    <div class="web"><svg class="icon"><use href="#i-web"/></svg><span>www.malereibetrieb-saber.de</span></div>
  </section>

  <section class="card back light">
    <div class="brand"><span class="brand-name">SABER</span></div>
    <div class="web"><svg class="icon"><use href="#i-web"/></svg><span>www.malereibetrieb-saber.de</span></div>
  </section>
</main>
</body>
</html>
```